White Paper and One-Page Advertisement for TELVAMORE-QX

I need both documents to be better formatted and designed so they look professional, not something someone with mediocre word skills put together. They will go out to 1000s of industry professionals, and they need to look sharp. I need them to have my company's color palate logo, and branding on it similar to how it is now, but better. Please do not change any of the written content, but it can be arranged in any other format you think is better. Smart art and things i've already used can be omitted in favor of better designs. The developer is free to use their creativity. White paper should not be longer than the three pages unless necessary.

Target Market(s)

Life Sciences supply chain professionals

Colors
33b8a4
0592cd
9bcb3c
fbee3e
3277b5

Requirements
Must have
• Must be professional looking and not look like something done in word. Please use the color palate as seen on the documents.
Should not have
• Any changes to the written content.

```html
<!DOCTYPE html>
<html lang="en">
<head>
<meta charset="utf-8">
<title>Changing Pharma's Paradigm of Waste – TELVAMORE-QX</title>
<link href="https://fonts.googleapis.com/css2?family=Raleway:wght@400;500;600;700&display=swap" rel="stylesheet">
<style>
:root{
  --green:#8cc63f;
  --lime:#c5cc3a;
  --deep-teal:#1a7a6d;
  --teal:#33b8a4;
  --sky:#48b6cc;
  --blue:#0592cd;
  --ink:#3b3b3b;
  --head:#111;
  --accent:#7ab92e;
  --wash:#f3f4f0;
  --panel:#eef5e1;
  --rule:#dfe5d6;
}
*{margin:0;padding:0;box-sizing:border-box}
html,body{width:1200px;height:849px;overflow:hidden;background:#fff}
body{font-family:"Raleway",sans-serif;color:var(--ink);font-size:7.6px;line-height:9.7px}
.spread{position:relative;width:1200px;height:849px}
.page{position:absolute;top:0;width:600px;height:849px}
.page--left{left:0}
.page--right{left:600px}
.abs{position:absolute}
.running-head{position:absolute;top:32px;height:16px;width:292px;background:#f1f1f1;display:flex;align-items:center;font-size:9.6px;color:#8cc63f;letter-spacing:.1px}
.running-head::before{content:"";width:16px;height:16px;background:var(--green);margin-right:8px}
.brand{position:absolute;top:40px;display:flex;align-items:center;gap:4px;font-weight:700;font-size:8.4px;color:var(--deep-teal);letter-spacing:.2px}
.brand i{width:10px;height:10px;border-radius:50%;background:var(--green);display:block}
h2.section{position:absolute;font-size:14px;font-weight:700;color:var(--head);line-height:16px;letter-spacing:.1px}
h3.sub{font-size:11.4px;font-weight:600;color:var(--accent);line-height:14px;margin-bottom:2px}
p{text-align:justify}
.wash{position:absolute;left:0;top:112px;width:600px;height:164px;background:var(--wash)}
.dropcap{float:left;font-size:32px;line-height:26px;color:var(--green);margin:1px 3px 0 0;font-weight:400}
.stat{position:absolute;width:108px;height:38px;color:#fff;font-size:19px;font-weight:700;padding:8px 10px}
.stat--wide{width:127px}
.stat-label{position:absolute;width:130px;font-size:7.6px;line-height:9.5px}
.num-row{position:absolute;left:36px;width:255px;display:flex;align-items:center;background:#fff;border:1px solid #eee}
.num-row b{width:72px;align-self:stretch;display:flex;align-items:center;justify-content:center;background:#f4f6ef;color:var(--green);font-size:19px;font-weight:700}
.num-row span{padding-left:10px;width:170px}
.hilite{position:absolute;left:36px;top:359px;width:255px;height:31px;background:var(--green);color:#fff;padding:4px 0 0 8px;line-height:11px}
.hilite div::before{content:"›";display:inline-block;width:7px;height:7px;border-radius:50%;background:var(--deep-teal);color:#fff;font-size:7px;line-height:6px;text-align:center;margin-right:4px}
.hilite b{font-weight:700}
ul.ticks{list-style:none}
ul.ticks li{position:relative;padding-left:14px}
ul.ticks li::before{content:"›";position:absolute;left:0;top:1px;width:7.5px;height:7.5px;border-radius:50%;background:var(--teal);color:#fff;font-size:8px;line-height:6.5px;text-align:center;font-weight:700}
.baseline{position:absolute;left:309px;top:322px;width:291px;height:490px;background:var(--green);color:#fff;padding:4px 9px}
.baseline h4{font-size:11px;font-weight:500;line-height:13px;margin-top:10px}
.baseline h4:first-child{margin-top:0}
.baseline h5{font-size:9px;font-weight:500;line-height:12px}
.baseline h6{font-size:7.6px;font-weight:700;line-height:10px;margin-top:4px;color:#1d3b14}
.baseline ul.ticks li{color:#1f3a12}
.baseline ul.ticks li::before{background:#fff;color:var(--green)}
.influence{position:absolute;left:636px;top:210px;width:256px;height:236px;background:var(--panel)}
.influence .spine{position:absolute;left:0;top:0;width:26px;height:236px;background:#dbe8c3}
.influence .spine span{position:absolute;left:13px;top:118px;transform:translate(-50%,-50%) rotate(-90deg);white-space:nowrap;font-size:12.6px;font-weight:700;color:var(--deep-teal);letter-spacing:.3px}
.driver{position:absolute;left:34px;width:221px;height:42px;color:#fff;font-size:17px;font-weight:600;display:flex;align-items:center;padding-left:8px;gap:6px}
.driver::before{content:"›";width:14px;height:14px;border-radius:50%;background:#fff;color:var(--deep-teal);font-size:14px;line-height:12px;text-align:center;font-weight:700;flex:none}
.barriers{position:absolute;left:904px;top:348px;width:296px;height:458px;background:var(--panel)}
.barrier-tag{position:absolute;left:13px;width:236px;height:22px;color:#fff;font-size:9.6px;font-weight:600;display:flex;align-items:center;padding-left:5px;gap:4px}
.barrier-tag::before{content:"›";width:9px;height:9px;border-radius:50%;background:#fff;color:var(--green);font-size:9px;line-height:7.5px;text-align:center;font-weight:700}
.barrier-text{position:absolute;left:13px;width:236px}
.footer-rule{position:absolute;top:826px;height:1px}
.folio{position:absolute;top:824px;font-size:7px;color:var(--teal)}
</style>
</head>
<body>
<div class="spread">

<!-- LEFT PAGE -->
<section class="page page--left">
  <div class="running-head" style="left:36px">CHANGING PHARMA'S PARADIGM OF WASTE</div>
  <div class="brand" style="left:490px"><i></i>TELVAMORE-QX</div>

  <div class="wash"></div>
  <h2 class="section" style="left:36px;top:96px">OVERVIEW</h2>
  <p class="abs" style="left:36px;top:123px;width:256px"><span class="dropcap">D</span>emand volatility is a challenge for very supply chain. It strikes at the end of supply chains causing a "bullwhip effect" that becomes exponentially more impactful further back in the chain. For Pharma, the effect is strongest in manufacturing and procurement, specifically with starting raw materials and consumables. Swings in demand can cripple launches, cause stock-outs, inflate material prices, make lean planning ineffective, and cause significant write-downs of residual/obsolete materials; ultimately inflating CoGS and reducing net income. These swings can also cause inventory costs to inflate, materials to expire or become obsolete, higher disposal fees, and a larger carbon footprint. The yearly financial impacts are staggering considering Pharma's economic footprint. Twenty of Pharma's top 100 companies were sampled using 2015 &amp; 2016 financial figures<sup style="font-size:4px">1-2-3-4</sup>. Industry estimates for waste include:</p>

  <div class="stat" style="left:309px;top:112px;background:var(--green)">3.77%</div>
  <div class="stat stat--wide" style="left:436px;top:112px;background:var(--lime)">$2.7B</div>
  <div class="stat-label" style="left:309px;top:157px">Avg Raw Material Write-down as a % of Net Income</div>
  <div class="stat-label" style="left:436px;top:157px">Est Pharma Written Down Inventory in 2016</div>
  <div class="stat" style="left:309px;top:203px;background:var(--deep-teal)">$2,034</div>
  <div class="stat stat--wide" style="left:436px;top:203px;background:var(--teal)">01</div>
  <div class="stat-label" style="left:309px;top:249px">Est US Pharma Revenue per 1 Ton Non-MSW Waste</div>
  <div class="stat-label" style="left:436px;top:249px">Correlation Coefficent of Material Write-downs and Firm Size</div>

  <h2 class="section" style="left:36px;top:299px">WHAT DO THESE NUMBERS MEAN?</h2>
  <div class="num-row" style="top:322px;height:30px"><b>3.77%</b><span>is an alarmingly high, and does not include capitalized consumables, equipment disposal, and similar wastes</span></div>
  <div class="hilite">
    <div><b>$5B</b> in net income LS Firm: est $185M in write-downs</div>
    <div><b>$50M</b> in net income LS Firm: est $1.9M in write-downs</div>
  </div>
  <div class="num-row" style="top:398px;height:32px"><b>$2.7B</b><span>is likely much lower than the real figure due to capitalizing consumable inventories for launches etc.</span></div>
  <div class="num-row" style="top:436px;height:28px"><b>01</b><span>correlation coefficient means this problem does not discriminate based on company size and is ubiquitous in the industry.</span></div>
  <div class="num-row" style="top:470px;height:32px"><b>$2,034</b><span>to one ton of industrial waste is not progressive.</span></div>

  <div class="abs" style="left:36px;top:509px;width:256px">
    <p>Industries have attempted to mitigate the bullwhip effect through many techniques and systems such as ERP, robust forecasting models, demand management, LSS tools, strategic sourcing, etc. However, life science firms still struggle to effectively address this problem as evidenced by the write-down figures. Many non-FDA regulated industries have started utilizing marketplaces and brokerage services to create circular supply chains that optimize waste by connecting buyers and sellers. However, Pharma and life sciences have yet to adopt this waste-centric supply chain and execute it in a manner conducive to the compliance and indemnification requirements of the industry regarding primary and secondary transactions of raw materials, equipment, consumables, spare parts, and collaborative relationships. Finished products such as APIs, intermediates, and devices are out of scope for this supply chain.</p>
    <p style="margin-top:7px">A life sciences marketplace and consortium for manufacturers, researchers, and vendors can minimize the aforementioned problems by quickly, innovatively, and transparently exchanging material information in safe and controlled environment ensuring a firm's standards for data integrity, cGMP compliance, contractual indemnification, and financial benefits are met; all by leveraging core auditing skills.</p>
    <p style="margin-top:7px">It is a call to arms among supply chain, procurement, and quality leaders to take part in a more circular, greener, and collaborative supply chain. Time is critical as global competition grows, customer and government emphasis on lowering pricing mounts5, and collective pressure on sustainability demands widespread action.</p>
    <p style="margin-top:7px">Let's explore Current and Future State of this industry issue to understand why such a marketplace can begin the much-needed transition for life science companies.</p>
  </div>

  <h2 class="section" style="left:309px;top:299px">BASELINE PROBLEM</h2>
  <div class="baseline">
    <h4>WHAT?</h4>
    <ul class="ticks">
      <li>Disposal of high quality materials, equipment, spare parts</li>
      <li>Single and/or limited sources of supply</li>
      <li>Inability to collaborative with like-minded life sciences firms</li>
      <li>High CoGS due to materials write-downs</li>
      <li>High inventory carrying costs</li>
      <li>Greater business continuity risk</li>
      <li>High disposal costs</li>
      <li>Larger environmental footprint</li>
      <li>Stock-out of materials</li>
    </ul>
    <h4 style="margin-top:12px">WHO?</h4>
    <ul class="ticks"><li>FDA Regulated Industries, Procurement, Quality, Production, and Finance.</li></ul>
    <h4 style="margin-top:12px">WHERE &amp; WHEN</h4>
    <ul class="ticks">
      <li>Commercial &amp; clinical production, R&amp;D, sourcing/purchasing, production planning, quality testing, etc.</li>
      <li>Volatile demand periods, e.g., product intro growth, decline, seasonality, economic uncertainty, and unforeseen events.</li>
    </ul>
    <h4 style="margin-top:12px">HOW DO WE KNOW IT'S THERE?</h4>
    <ul class="ticks"><li>We physically see it taking place, and it's in our data.</li></ul>
    <h4 style="margin-top:14px">TRIPLE BOTTOM LINE IMPACT</h4>
    <h5>Financial</h5>
    <h6>Vendors/ Sellers</h6>
    <ul class="ticks"><li>Higher write-downs/offs and 3rd party disposal fees</li></ul>
    <h6 style="margin-top:9px">Vendors/ Sellers</h6>
    <ul class="ticks">
      <li>Lost sales – stock-outs</li>
      <li>Inflated market value of materials &amp; supplier expedition fees</li>
      <li>High SS cost due to bullwhip effect</li>
    </ul>
    <h4 style="margin-top:9px">ENVIRONMENT</h4>
    <ul class="ticks">
      <li>Greater contribution to global warming through landfill addition, incineration, inactivation, and energy consumption.</li>
      <li>Noncompliance with ISO 14000 &amp; 9000 and B-Corp Status</li>
    </ul>
    <h4 style="margin-top:11px">SOCIETY</h4>
    <ul class="ticks">
      <li>Lost community trust - high environment and consumer costs</li>
      <li>Less Innovation, collaboration, and supply chain optimization</li>
    </ul>
  </div>

  <div class="footer-rule" style="left:76px;width:50px;background:var(--teal)"></div>
  <div class="footer-rule" style="left:132px;width:468px;background:var(--green)"></div>
  <div class="folio" style="left:37px">2</div>
</section>

<!-- RIGHT PAGE -->
<section class="page page--right">
  <div class="running-head" style="left:37px">CHANGING PHARMA'S PARADIGM OF WASTE</div>
  <div class="brand" style="left:490px"><i></i>TELVAMORE-QX</div>
  <div class="footer-rule" style="left:0;width:468px;background:var(--green)"></div>
  <div class="footer-rule" style="left:474px;width:50px;background:var(--teal)"></div>
  <div class="folio" style="left:560px">3</div>
</section>

<h2 class="section" style="left:636px;top:96px">CURRENT STATE</h2>
<div class="abs" style="left:636px;top:117px;width:256px">
  <h3 class="sub">External Solutions</h3>
  <p>Pharma and other FDA industries spend considerable energy on reducing waste. A plethora of techniques are employed to mitigate, prepare for, respond to, and recover from the bullwhip effect, which is one of the leading causes of write-downs and waste. However, such efforts are predicated on:</p>
</div>

<div class="influence">
  <div class="spine"><span>BULLWHIP INFLUENCES</span></div>
  <div class="driver" style="top:10px;background:var(--green)">Forecast Accuracy</div>
  <div class="driver" style="top:67px;background:var(--lime)">Supplier Reliability</div>
  <div class="driver" style="top:125px;background:var(--deep-teal)">Process Variability</div>
  <div class="driver" style="top:184px;background:var(--teal)">External Enivronment</div>
</div>

<p class="abs" style="left:636px;top:462px;width:256px">While not fruitless, attempts to mitigate the above external influences are extremely unpredictable and have never solved pharma's write-down, inefficiency, stock-out, and environmental problems.</p>

<div class="abs" style="left:636px;top:529px;width:256px">
  <h3 class="sub">Internal Solutions</h3>
  <p>The next effort involves reducing obsolescence by making use of materials within the firm. Typically, interplant demand is the only outlet to optimize surplus earmarked for a reserve/write-down. Even this involves many of the same regulatory compliance, quality, and economic challenges. Facilitating this takes time, resources, and does not provide a broad network to utilize.</p>
  <h3 class="sub" style="margin-top:8px">Environmental Solutions</h3>
  <p>FDA industries, like most others, make attempts to reuse, recycle, and convert to energy where applicable. However, they're unable to conduct these activities for perishable, expiring, and/or consumable materials.</p>
  <h3 class="sub" style="margin-top:8px">Undesirable Solutions</h3>
  <p>Unfortunately, third party disposal (frequently landfill) is typically the first and most popular option as perishable, expiring, and complex materials are generally unable to be reused or recycled. These disposals come in many forms to include responsible landfills, incineration, inactivation, etc.</p>
  <h3 class="sub" style="margin-top:8px">Overall</h3>
  <p>Industries spend much capital and resources to reduce write-downs in an environment where the bullwhip effect reigns supreme. Mitigations to this effect are attempted but only partially successful or sustainable.</p>
</div>

<h2 class="section" style="left:909px;top:96px">REFINED PROBLEM</h2>
<p class="abs" style="left:909px;top:114px;width:256px">There is no clear market leader that helps organizations optimize waste, collaborative to reduce it, and market more quality materials to more firms whether for research, manufacturing, or donations. This marketplace must be regulated and all participates properly vetted and authenticated. Accounts must be created to enable companies to post materials and request for information/quotes. Additionally, this marketplace must facilitate collaborative relationships between companies that help them reduce supply chain costs. It must quickly, economically, compliantly, and legally facilitate those exchanges. Lack of this market leader may have enabled the waste problem as seen today.</p>

<div class="abs" style="left:909px;top:239px;width:262px">
  <h3 class="sub">Contemporary Operating Environment</h3>
  <ul class="ticks">
    <li>Constant pressure from global competition, increasing customer and governmental demand on price, more regulatory scrutiny, and a relentless societal pursuit of sustainability are starting to erode what were once high margins for Pharma6.</li>
    <li>Regulators are cooperative and open to solutions.</li>
    <li>Exchanges and consortiums are not typically leveraged in Pharma.</li>
    <li>Pharma continues to struggle with the bullwhip effect.</li>
  </ul>
</div>

<div class="barriers">
  <h2 class="section" style="left:13px;top:10px">BARRIERS</h2>
  <div class="barrier-tag" style="top:36px;background:var(--green)">Compliance</div>
  <ul class="ticks barrier-text" style="top:64px"><li>It is the responsibility of manufacturers to provide customers/patients with quality, safe, and efficacious products. However, there is a misperception that high quality cGMP compliant materials, parts, and equipment cannot be sourced from aftermarket exchanges and consortiums.</li></ul>
  <div class="barrier-tag" style="top:122px;background:var(--lime)">Liability</div>
  <ul class="ticks barrier-text" style="top:152px"><li>Contractual agreements with suppliers have clauses to resolve issues dealing with poor quality. There is a misperception that these agreements cannot implemented at both the marketplace and transactionactional level.</li></ul>
  <div class="barrier-tag" style="top:198px;background:var(--deep-teal)">Economics</div>
  <ul class="ticks barrier-text" style="top:226px"><li>Exchanges can be difficult due to time/effort. A sanctioned marketplace can provide the structure to make it easy.</li></ul>
  <div class="barrier-tag" style="top:256px;background:var(--sky)">Sustainability</div>
  <ul class="ticks barrier-text" style="top:284px"><li>Firms have not discovered how to leverage exchanges to reduce environmental footprint and enable industry certifications as well as community trust.</li></ul>
  <div class="barrier-tag" style="top:324px;background:var(--blue)">Confidence</div>
  <ul class="ticks barrier-text" style="top:354px"><li>Trust is critical to firms. They should know that a marketplace has properly vetted members with KPI data for analysis.</li></ul>
  <div class="barrier-tag" style="top:394px;background:var(--green)">Speed</div>
  <ul class="ticks barrier-text" style="top:422px"><li>Exchanges should be fast. An innovative marketplace can ensure quick exchanges.</li></ul>
</div>

</div>
</body>
</html>
```